Australian small vineyard seeking wine label.

We need a wine label design for a new wine brand \Boutique winery - 2 vintages so far, looking for something a little eye catching, but simple.
Wine label name: Brent and Co
2013 Cabernet Shiraz
2014 Shiraz
Estate grown
Vineyard located at Larkridge in the Merrin Valley South Australia.

Target Market(s)

ladies aged between 20 and 50

Industry/Entity Type

Boutique

Logo Text

Brent and Co

Logo styles of interest
Emblem Logo
Pictorial/Combination Logo
Abstract Logo
Character Logo
Font styles to use
Serif
Script

Requirements
Must have
• easy to read text
Nice to have
• The grape grower and winemaker is Martin Brent -
• had some thoughts of Captain Brent - Australian - naval flag
• But very open to ideas
Should not have
• over complications and colors due to cost of wine label being determined by amount of colors required abd print set up.

```html
<!DOCTYPE html>
<html lang="en">
<head>
<meta charset="utf-8">
<title>Brent and Co – Cabernet Shiraz 2013 Label</title>
<link rel="stylesheet" href="https://fonts.googleapis.com/css2?family=Cinzel:wght@400&display=swap">
<style>
  :root {
    --page: #ececec;
    --label: #ffffff;
    --violet: #4b3d98;
    --violet-deep: #3f3477;
    --band-text: #ffffff;
  }
  * { margin: 0; padding: 0; box-sizing: border-box; }
  html, body {
    width: 973px;
    height: 1200px;
    overflow: hidden;
    background: var(--page);
  }
  .canvas {
    position: relative;
    width: 973px;
    height: 1200px;
  }
  .label {
    position: absolute;
    left: 87px;
    top: 180px;
    width: 800px;
    height: 840px;
    background: var(--label);
    box-shadow: 0 2px 10px rgba(0,0,0,0.08);
    font-family: "Cinzel", "Times New Roman", serif;
    font-weight: 400;
    color: var(--violet);
  }
  .brand-mark {
    position: absolute;
    left: 50%;
    top: 80px;
    width: 110px;
    height: 110px;
    margin-left: -55px;
    border: 5px solid var(--violet);
    border-radius: 50%;
  }
  .brand-name {
    position: absolute;
    left: 0;
    right: 0;
    top: 250px;
    text-align: center;
    font-size: 40px;
    font-weight: 400;
    letter-spacing: 8px;
    padding-left: 8px;
    line-height: 1;
    color: var(--violet);
  }
  .variety-band {
    position: absolute;
    left: 0;
    top: 410px;
    width: 800px;
    height: 200px;
  }
  .variety-band svg { display: block; }
  .variety {
    position: absolute;
    left: 0;
    right: 0;
    top: 480px;
    text-align: center;
    color: var(--band-text);
    font-size: 38px;
    font-weight: 400;
    letter-spacing: 7px;
    padding-left: 7px;
    line-height: 1;
  }
  .vintage {
    position: absolute;
    right: 100px;
    top: 530px;
    color: var(--band-text);
    font-size: 24px;
    letter-spacing: 5px;
    line-height: 1;
  }
  .origin {
    position: absolute;
    left: 0;
    right: 0;
    top: 672px;
    text-align: center;
    color: var(--violet-deep);
    font-size: 25px;
    letter-spacing: 6px;
    line-height: 38px;
  }
  .origin p { padding-left: 6px; }
</style>
</head>
<body>
<div class="canvas">
  <section class="label">
    <div class="brand-mark"></div>
    <h1 class="brand-name">BRENT AND CO</h1>

    <div class="variety-band">
      <svg width="800" height="200" viewBox="0 0 800 200" aria-hidden="true">
        <path d="M0 18 C 200 -4, 420 4, 560 14 C 660 21, 740 12, 800 2
                 L 800 170 C 720 182, 640 186, 520 178 C 380 168, 200 176, 0 200 Z"
              fill="var(--violet)"/>
      </svg>
    </div>
    <h2 class="variety">CABERNET SHIRAZ</h2>
    <p class="vintage">2013</p>

    <div class="origin">
      <p>ESTATE GROWN</p>
      <p>LARKRIDGE | MERRIN VALLEY</p>
      <p>SOUTH AUSTRALIA</p>
    </div>
  </section>
</div>
</body>
</html>
```